Natural and organic skincare brand needs label design!

I need labels designed for my natural and organic skincare brand velmurine. The front of the bottles must contain the logo (image attached) and the following words: Formulated by a Naturopath; Anti-aging therapy; Organic Facial Oil; with CoEnzyme Q10 and Rosehip Seed Oil; 100ml e3.38fl.oz. Colours I would like used include black/white/grey/silver and aqua. I also like the grey woodgrain used on my draft website (check out www.velmurine.com.au). The logo should be silver foil (shiny).The final design should be simple and communicate nature and sophistication. Some designs I like are found in the attachments. I intend to use black or white bottles.

women aged 30-50 interested in natural products

Skin Care Product

Serif
Sans Serif
Decorative
Script
• Any

• Dimensions: 62mm (w) x 75mm (H) (front label only)
• Must contain the logo (image attached). The logo should be silver foil (shiny). and the following words are to be included on the label:
• Formulated by a Naturopath;
• Anti-aging Therapy;
• Organic Facial Oil;
• with CoEnzyme Q10 and Rosehip Seed Oil;
• 100ml e3.38fl.oz.
• Colours I would like used include black/white/grey/silver and aqua (turquoise). But I am also open to suggestion. I also like the grey woodgrain used on my draft website (check out www.velmurine.com.au)

```html
<!DOCTYPE html>
<html lang="en">
<head>
<meta charset="utf-8">
<title>velmurine – Anti-Aging Therapy Label</title>
<link rel="stylesheet" href="https://fonts.googleapis.com/css2?family=Raleway:wght@300;400;500&display=swap">
<style>
  :root {
    --backdrop: #efefef;
    --label-white: #ffffff;
    --slate: #47505c;
    --ink: #3e444c;
    --aqua: #40cfd6;
    --grain-light: #e6e6e4;
    --grain-dark: #c9c9c6;
    --muted: #6d737a;
  }
  * { margin: 0; padding: 0; box-sizing: border-box; }
  html, body {
    width: 1200px;
    height: 1030px;
    overflow: hidden;
    background: var(--backdrop);
    font-family: "Raleway", sans-serif;
  }
  .canvas {
    position: relative;
    width: 1200px;
    height: 1030px;
  }
  .front-label {
    position: absolute;
    left: 220px;
    top: 55px;
    width: 760px;
    height: 920px;
    background: var(--label-white);
    box-shadow: 0 2px 14px rgba(0,0,0,0.06);
    display: flex;
    flex-direction: column;
    align-items: center;
    color: var(--ink);
  }
  .woodgrain-band {
    position: absolute;
    left: 0;
    top: 70px;
    width: 100%;
    height: 150px;
    background: linear-gradient(180deg, var(--grain-light) 0%, var(--grain-dark) 45%, var(--grain-light) 100%);
  }
  .brand-seal {
    position: relative;
    margin-top: 48px;
    width: 194px;
    height: 194px;
    border-radius: 50%;
    background: var(--slate);
    display: flex;
    align-items: center;
    justify-content: center;
    color: #ffffff;
    font-weight: 400;
    font-size: 30px;
    letter-spacing: 3px;
  }
  .product-title {
    margin-top: 60px;
    text-align: center;
    font-weight: 300;
    line-height: 1;
  }
  .product-title .line-one {
    display: block;
    font-size: 66px;
    letter-spacing: 1px;
  }
  .product-title .line-two {
    display: block;
    font-size: 88px;
    margin-top: 6px;
  }
  .aqua-rule {
    width: 560px;
    height: 2px;
    background: var(--aqua);
  }
  .title-rule { margin-top: 14px; }
  .product-type {
    margin-top: 14px;
    color: var(--aqua);
    font-weight: 500;
    font-size: 34px;
    letter-spacing: 4px;
  }
  .key-ingredients {
    margin-top: 6px;
    font-size: 19px;
    color: var(--muted);
    font-weight: 400;
  }
  .botanical-sketch {
    margin-top: 40px;
    width: 230px;
    height: 160px;
    border-radius: 6px;
    background: radial-gradient(ellipse at center, #dadde0 0%, #f3f4f5 70%, #ffffff 100%);
  }
  .maker-note {
    margin-top: 46px;
    font-size: 30px;
    font-weight: 400;
  }
  .maker-rule { margin-top: 10px; }
  .volume {
    margin-top: 14px;
    font-size: 20px;
    color: var(--muted);
  }
</style>
</head>
<body>
  <main class="canvas">
    <section class="front-label">
      <div class="woodgrain-band" role="img" aria-label="Grey woodgrain texture band"></div>
      <div class="brand-seal">velmurine</div>
      <h1 class="product-title">
        <span class="line-one">ANTI-AGING</span>
        <span class="line-two">THERAPY</span>
      </h1>
      <div class="aqua-rule title-rule"></div>
      <p class="product-type">ORGANIC FACIAL OIL</p>
      <p class="key-ingredients">with CoEnzyme Q10 and Rosehip Seed Oil</p>
      <div class="botanical-sketch" role="img" aria-label="Line drawing of orchid flowers on a stem"></div>
      <p class="maker-note">Formulated by a Naturopath</p>
      <div class="aqua-rule maker-rule"></div>
      <p class="volume">100ml e3.38fl.oz</p>
    </section>
  </main>
</body>
</html>
```